Trovadel Ltda

Logo design focused on: - Construction of civil works - Electrical services - Metal structures - Equipment rental Tomas Ibarra Luque Manager trovadel.ltda@norvexmail.com 56 9 41827035 Quirobamba s / n, Tolvas, Villa Orlen de Cumaro

Target Market(s)

Building

Colors
33a6d7
0292cd
33b8a4
0555a3

```html
<!DOCTYPE html>
<html lang="es">
<head>
<meta charset="utf-8">
<title>Trovadel Ltda – Tarjeta de presentación</title>
<link rel="stylesheet" href="https://fonts.googleapis.com/css2?family=Montserrat:wght@400;500;600;700&display=swap">
<style>
  :root {
    --sky: #33a6d7;
    --blue: #0292cd;
    --teal: #33b8a4;
    --blue-deep: #0555a3;
    --band: #0f74c0;
    --ink: #1d1d1d;
    --paper: #ffffff;
    --backdrop: #e9ecef;
  }
  * { margin: 0; padding: 0; box-sizing: border-box; }
  html, body {
    width: 1200px; height: 837px; overflow: hidden;
    background: var(--backdrop);
    font-family: "Montserrat", sans-serif;
  }
  .card {
    position: absolute; left: 75px; top: 118px;
    width: 1050px; height: 600px;
    background: var(--paper);
    border-radius: 30px;
    overflow: hidden;
    box-shadow: 0 10px 30px rgba(0,0,0,.12);
  }
  .card__waves { position: absolute; inset: 0; }
  .brand {
    position: absolute; left: 110px; top: 150px;
    display: flex; align-items: center; gap: 22px;
  }
  .brand__dot {
    width: 92px; height: 92px; border-radius: 50%;
    background: var(--blue);
    flex: none;
  }
  .brand__name {
    font-size: 46px; font-weight: 600; letter-spacing: 1px;
    color: var(--blue-deep);
    white-space: nowrap;
  }
  .divider {
    position: absolute; left: 585px; top: 150px;
    width: 2px; height: 250px; background: var(--ink);
  }
  .contact { position: absolute; left: 625px; top: 160px; }
  .contact__name { font-size: 30px; font-weight: 700; color: var(--blue-deep); white-space: nowrap; }
  .contact__role { font-size: 20px; font-weight: 500; color: var(--teal); margin-top: 2px; }
  .contact__list { list-style: none; margin-top: 26px; }
  .contact__item {
    display: flex; align-items: center; gap: 10px;
    font-size: 19px; color: var(--ink); line-height: 30px;
    white-space: nowrap;
  }
  .contact__item svg { width: 18px; height: 18px; fill: var(--ink); flex: none; }
  .contact__address { font-size: 19px; color: var(--ink); line-height: 28px; margin-top: 18px; white-space: nowrap; }
</style>
</head>
<body>
  <article class="card">
    <svg class="card__waves" viewBox="0 0 1050 600" preserveAspectRatio="none" aria-hidden="true">
      <path d="M0,330 C260,430 620,470 1050,600 L0,600 Z" fill="var(--band)"/>
      <path d="M0,290 C280,400 640,450 1050,585" fill="none" stroke="var(--teal)" stroke-width="9"/>
      <path d="M0,270 C290,385 660,430 1050,570" fill="none" stroke="var(--teal)" stroke-width="6"/>
      <path d="M0,305 C280,415 640,462 1050,595" fill="none" stroke="var(--paper)" stroke-width="6"/>
    </svg>

    <div class="brand">
      <span class="brand__dot"></span>
      <span class="brand__name">Trovadel Ltda</span>
    </div>

    <span class="divider"></span>

    <section class="contact">
      <h1 class="contact__name">Tomas Ibarra Luque</h1>
      <p class="contact__role">Gerente</p>
      <ul class="contact__list">
        <li class="contact__item">
          <svg viewBox="0 0 24 24"><path d="M2 5h20v14H2z M3 6l9 7 9-7" fill="none" stroke="#1d1d1d" stroke-width="2"/></svg>
          trovadel.ltda@norvexmail.com
        </li>
        <li class="contact__item">
          <svg viewBox="0 0 24 24"><path d="M6.6 10.8a15 15 0 0 0 6.6 6.6l2.2-2.2c.3-.3.7-.4 1-.2 1.1.4 2.3.6 3.6.6.6 0 1 .4 1 1V20c0 .6-.4 1-1 1A17 17 0 0 1 3 4c0-.6.4-1 1-1h3.5c.6 0 1 .4 1 1 0 1.3.2 2.5.6 3.6.1.3 0 .7-.2 1z"/></svg>
          +56 9 41827035
        </li>
      </ul>
      <p class="contact__address">Quirobamba s/n, Tolvas,<br>Villa Orlen de Cumaro</p>
    </section>
  </article>
</body>
</html>
```